Vek Factory Sticker design

Hello, We are a Doner Kebab Factory, We need sticker design for the following:
1-Sticker for the product details. (look to the attached picture) to stick it on the Doner.
2-Lebel Sticker for the product type, for example ( Premium, Standard and Customised). please check the attached picture,
Don't make the design exactly same as the attachment picture, But try to make something that keeps the same idea but deferent.
Use the same colors of the Logo. but for the lebels you can use other colors
Make it professional design.
Target Market(s)
Restaurant and supermarket
Industry/Entity Type
Factory
Look and feel

```html
<!DOCTYPE html>
<html lang="en">
<head>
<meta charset="utf-8">
<title>Vek Factory – Gold Label Sticker</title>
<link href="https://fonts.googleapis.com/css2?family=Baloo+2:wght@800&family=Lato:ital,wght@0,400;0,700;0,900;1,700;1,900&display=swap" rel="stylesheet">
<style>
  :root{
    --gold:#c9962a;
    --gold-deep:#a9781c;
    --gold-light:#f3d38a;
    --gold-pale:#fbe6ad;
    --cream:#fdf0e0;
    --cream-soft:#fdf6ea;
    --box-line:#f1dcb5;
    --sun:#fce291;
    --text-gold:#d4a23a;
    --foot-gold:#b8862a;
    --web-red:#b51d22;
    --pattern:#f4f0ea;
  }
  html,body{margin:0;padding:0;overflow:hidden;background:#fff;}
  .sticker{position:relative;width:900px;height:1200px;overflow:hidden;background:#fff;font-family:"Lato",sans-serif;}
  .sticker__shapes{position:absolute;inset:0;}
  .brand{position:absolute;left:300px;width:300px;top:112px;display:flex;align-items:center;justify-content:center;gap:10px;}
  .brand__mark{width:16px;height:16px;border-radius:50%;background:var(--gold);flex:none;}
  .brand__name{font-family:"Lato",sans-serif;font-weight:900;font-size:28px;letter-spacing:0.5px;color:var(--gold-deep);white-space:nowrap;}
  .label-title{position:absolute;left:0;width:900px;top:318px;text-align:center;
    font-family:"Baloo 2",sans-serif;font-weight:800;font-size:78px;line-height:1;
    letter-spacing:-2px;color:var(--gold-pale);
    text-shadow:
      2px 0 0 var(--gold),-2px 0 0 var(--gold),0 2px 0 var(--gold),0 -2px 0 var(--gold),
      2px 2px 0 var(--gold),-2px 2px 0 var(--gold),2px -2px 0 var(--gold),-2px -2px 0 var(--gold),
      0 5px 0 var(--gold),2px 6px 0 var(--gold-deep),-2px 6px 0 var(--gold-deep);}
  .label-tier{position:absolute;left:0;width:900px;top:418px;text-align:center;
    font-weight:900;font-style:italic;font-size:30px;color:var(--gold);white-space:nowrap;}
  .label-tier .stars{font-style:normal;font-size:20px;letter-spacing:5px;vertical-align:4px;margin:0 8px;}
  .label-code{position:absolute;left:0;width:900px;top:466px;text-align:center;
    font-weight:900;font-style:italic;font-size:14px;color:var(--gold);}
  .field{position:absolute;font-weight:900;font-style:italic;font-size:12px;color:var(--text-gold);}
  .product-notes{position:absolute;left:212px;width:476px;top:840px;margin:0;
    font-size:14.5px;line-height:19px;text-align:justify;color:var(--text-gold);}
  .product-notes p{margin:0;}
  .product-notes p + p{padding-left:6px;}
  .product-notes b{font-weight:900;}
  .contact{position:absolute;left:0;width:900px;top:1096px;text-align:center;
    font-weight:700;font-size:11px;line-height:12.5px;color:var(--foot-gold);}
  .contact .web{color:var(--web-red);}
</style>
</head>
<body>
<main class="sticker">
  <svg class="sticker__shapes" width="900" height="1200" viewBox="0 0 900 1200" xmlns="http://www.w3.org/2000/svg">
    <g class="chevrons chevrons--left">
      <polygon points="225,88 250,88 205,135 250,182 225,182 180,135" fill="var(--gold-pale)"/>
      <polygon points="255,88 280,88 235,135 280,182 255,182 210,135" fill="var(--gold-light)"/>
      <polygon points="270,88 300,88 255,135 300,185 270,185 225,135" fill="var(--gold)"/>
    </g>
    <g class="chevrons chevrons--right">
      <polygon points="675,88 650,88 695,135 650,182 675,182 720,135" fill="var(--gold-pale)"/>
      <polygon points="645,88 620,88 665,135 620,182 645,182 690,135" fill="var(--gold-light)"/>
      <polygon points="630,88 600,88 645,135 600,185 630,185 675,135" fill="var(--gold)"/>
    </g>
    <path class="arch" d="M292,200 L292,130 Q292,44 450,44 Q608,44 608,130 L608,200" fill="#fff" stroke="var(--gold)" stroke-width="14"/>
    <path class="arch-dots" d="M292,200 L292,130 Q292,44 450,44 Q608,44 608,130 L608,200" fill="none" stroke="#fff" stroke-width="4" stroke-linecap="round" stroke-dasharray="0.5 11"/>
    <path class="body" d="M178,490 L722,490 L688,1135 Q686,1152 668,1152 L232,1152 Q214,1152 212,1135 Z" fill="#fff" stroke="var(--gold)" stroke-width="5"/>
    <path class="body-wave" d="M207,1045 Q450,1095 693,1040 L688,1135 Q686,1152 668,1152 L232,1152 Q214,1152 212,1135 Z" fill="var(--sun)"/>
    <rect class="top-panel" x="158" y="198" width="584" height="120" rx="24" fill="var(--pattern)" stroke="var(--gold)" stroke-width="6" role="img" aria-label="Soft geometric ornament pattern"/>
    <g class="hanging-cords" stroke="var(--gold)" stroke-width="2">
      <line x1="203" y1="204" x2="203" y2="300"/>
      <line x1="697" y1="204" x2="697" y2="300"/>
    </g>
    <path class="banner" d="M122,272 L445,300 L778,272 Q808,270 808,300 L808,458 Q808,488 778,490 L450,515 L122,490 Q92,488 92,458 L92,300 Q92,270 122,272 Z" fill="var(--cream)" stroke="var(--gold)" stroke-width="8"/>
    <circle cx="203" cy="301" r="4" fill="#6b4a1e"/>
    <circle cx="697" cy="301" r="4" fill="#6b4a1e"/>
    <g class="tier-rules" stroke="var(--gold-light)" stroke-width="1.5">
      <line x1="188" y1="414" x2="712" y2="414"/>
      <line x1="188" y1="457" x2="712" y2="457"/>
    </g>
    <g class="fields" fill="var(--cream-soft)" stroke="var(--box-line)" stroke-width="1.5">
      <rect x="190" y="540" width="518" height="176" rx="14"/>
      <rect x="205" y="726" width="149" height="99" rx="12"/>
      <rect x="376" y="726" width="146" height="99" rx="12"/>
      <rect x="544" y="726" width="152" height="99" rx="12"/>
    </g>
  </svg>

  <div class="brand"><span class="brand__mark"></span><span class="brand__name">Vek Factory</span></div>

  <div class="label-title">GOLD LABEL</div>
  <div class="label-tier"><span class="stars">★★★★★</span>PREMIUM QUALITY<span class="stars">★★★★★</span></div>
  <div class="label-code">UK DV020 EC</div>

  <div class="field" style="left:200px;top:552px">CUSTOMER :</div>
  <div class="field" style="left:213px;top:738px">CUSTOMER :</div>
  <div class="field" style="left:388px;top:738px">CUSTOMER :</div>
  <div class="field" style="left:555px;top:738px">CUSTOMER :</div>

  <section class="product-notes">
    <p><b>Quare talis :</b> improborum consensio non modo excusatione amicitiae tegenda non est sed potius supplicio omni vindicanda est, ut ne quis concessum putet amicum vel bellum patriae inferentem sequi; quod autem non minori curae est, qualis res publica post mortem meam.</p>
    <p><b>Quare talis :</b> res ire coepit, haud scio an aliquando futurum sit. Mihi autem non minori curae est, qualis res publica post mortem meam.autem non minori curae est, qualis res publica post mortem meam.autem non minori curae est, qualis res publica post mortem.</p>
    <p><b>Quare talis :</b> res ire coepit, haud scio an aliquando futurum sit. Mihi autem non minori curae est, qualis res publica post mortem meam.</p>
  </section>

  <footer class="contact">
    non minori curae est, qualis res publica post mortem meam futura<br>
    Tél : 210.480.390 - Fax : 210.480.390<br>
    <span class="web">www.VekDonerWorks.com</span>
  </footer>
</main>
</body>
</html>
```